TELVIRA Web Page

We need a corporate web site for a new company TELVIRA Corporation. TELVIRA is a technology company that has developed a new virtualization solution for corporate applications. Our target customers are IT professionals. We have a logo, which we will provide.

Final design should communicate: innovation, stability, professionalism

Industry/Entity Type

It Company

```html
<!DOCTYPE html>
<html lang="en">
<head>
<meta charset="utf-8">
<title>TELVIRA Corporation</title>
<link rel="stylesheet" href="https://fonts.googleapis.com/css2?family=Arimo:wght@400;700&family=Oswald:wght@400&display=swap">
<style>
  :root {
    --bg: #2b2926;
    --bg-deep: #1f1d1b;
    --photo-light: #b7b1a3;
    --photo-mid: #6e695f;
    --photo-dark: #1a1917;
    --accent: #ffdf00;
    --accent-dim: #5c5120;
    --brand-text: #d9d6cf;
    --footer-title: #c9c5bc;
    --footer-text: #5e5a54;
  }
  * { margin: 0; padding: 0; box-sizing: border-box; }
  html, body { width: 1200px; height: 690px; overflow: hidden; }
  body {
    position: relative;
    background: radial-gradient(ellipse 60% 70% at 50% 50%, #37342f 0%, var(--bg) 60%, var(--bg-deep) 100%);
    font-family: "Arimo", Arial, sans-serif;
  }
  .hero-visual {
    position: absolute;
    left: 192px; top: 202px;
    width: 846px; height: 333px;
    background:
      radial-gradient(ellipse 28% 45% at 50% 50%, var(--photo-dark) 0%, #2f2c28 45%, transparent 100%),
      radial-gradient(ellipse 55% 60% at 50% 50%, var(--photo-mid) 30%, var(--photo-light) 75%, rgba(120,114,102,0) 100%);
    -webkit-mask-image: linear-gradient(90deg, transparent 0%, #000 8%, #000 92%, transparent 100%);
    mask-image: linear-gradient(90deg, transparent 0%, #000 8%, #000 92%, transparent 100%);
  }
  .brand {
    position: absolute;
    left: 279px; top: 160px;
    font-size: 13px;
    color: var(--brand-text);
    letter-spacing: 0.2px;
  }
  .chevrons {
    position: absolute; left: 0; top: 0;
    width: 1200px; height: 690px;
  }
  .headline {
    position: absolute;
    left: 314px; top: 222px;
    font-size: 57px;
    line-height: 53px;
    font-weight: 400;
    color: var(--accent);
    letter-spacing: -0.5px;
    -webkit-text-stroke: 0.6px var(--accent);
  }
  .headline-dot {
    position: absolute;
    left: 299px; top: 233px;
    width: 15px; height: 15px;
    border-radius: 50%;
    background: var(--accent);
  }
  .footer {
    position: absolute;
    left: 450px; top: 551px;
    width: 325px;
    text-align: center;
  }
  .footer-title {
    font-family: "Oswald", "Arial Narrow", sans-serif;
    font-size: 8px;
    color: var(--footer-title);
    letter-spacing: 0.3px;
  }
  .footer-text {
    position: relative;
    margin-top: 12px;
    font-size: 8.8px;
    line-height: 11px;
    color: var(--footer-text);
  }
  .footer-text::before {
    content: "";
    position: absolute;
    left: 8px; top: 1px;
    width: 9px; height: 9px;
    border-radius: 50%;
    background: #3f3c37;
  }
</style>
</head>
<body>
  <div class="hero-visual" role="img" aria-label="Close-up photograph of a dandelion seed head, mirrored into a symmetrical radiating pattern"></div>

  <p class="brand">TELVIRA corp.</p>

  <svg class="chevrons" viewBox="0 0 1436 826" preserveAspectRatio="none" aria-hidden="true">
    <g stroke="var(--accent-dim)" stroke-width="5" fill="none" opacity="0.8">
      <line x1="848" y1="180" x2="882" y2="242"/>
      <line x1="908" y1="180" x2="942" y2="242"/>
      <line x1="968" y1="180" x2="1002" y2="242"/>
    </g>
    <g stroke="var(--accent)" stroke-width="5" fill="none" stroke-linejoin="miter">
      <polyline points="882,242 998,444 882,640"/>
      <polyline points="942,242 1058,444 942,640"/>
      <polyline points="1002,242 1118,444 1002,640"/>
    </g>
  </svg>

  <span class="headline-dot"></span>
  <h1 class="headline">A new<br>virtualization<br>solution for<br>corporate<br>applications</h1>

  <footer class="footer">
    <p class="footer-title">TELVIRA CORP. COPYRIGHT 2013</p>
    <p class="footer-text">Lorem ipsum dolor sit amet, consectetur adipiscing elit. Aenean pulvinar augue et tortor posuere, et adipiscing odio eleifend. Sed felis ipsum, consequat id lectus sed, ornare suscipit dolor. Phasellus varius pellentesque libero, sed porttitor ipsum accumsan ut. Nullam sed vulputate eros, nec lacinia felis.</p>
  </footer>
</body>
</html>
```